Brochure for people who suffer from Sleep Apnea and need a medical device called a CPAP Machine

I want a brochure that can be placed in doctors offices with my competitors brochures. It needs to be bold and stand out and deliver a very strong message that draws the patients away from our competitors and to us. I have included a word document generally outlining some of my requirements and thoughts, please review prior to investing time into design!

Target Market(s)

people who suffer from sleep apnea, which is a disease that causes them to stop breathing many times per hour, resulting in the patient needing to wear a device called a CPAP Machine. This is an illness that can impact anyone but is more likely to impact those suffering from obesity and men.

Industry/Entity Type

Health Care

Other font styles liked:
• Use what you think is best

Colors

Designer to choose colors to be used in the design.

Requirements
Must have
• Please see word document for must have items, and feel free to contact me with any questions.
• Also must have bold colors, and/or graphics to really stand out among my competitors brochures.
Nice to have
• Would prefer to use the baby picture titled "sleeping baby 4" if possible but provided 2 other baby photos just in case. Whatever you want to add, use your professional creativity! You Don't need to use all the pictures uploaded!!!!!
Should not have
• Nothing discriminatory or offensive.

```html
<!DOCTYPE html>
<html lang="en">
<head>
<meta charset="utf-8">
<title>RestWell Supply – Sleep Apnea Brochure</title>
<link href="https://fonts.googleapis.com/css2?family=Montserrat:ital,wght@0,400;0,500;0,600;0,700;0,800;1,500;1,700;1,800&display=swap" rel="stylesheet">
<style>
:root{
  --green:#2f8a3c;
  --green-dark:#1e6a2b;
  --purple:#4a2a5c;
  --purple-mid:#6b3f80;
  --purple-soft:#8a5c9c;
  --cream:#f1e4c6;
  --gold:#f2b705;
  --white:#ffffff;
  --ink:#2a2a2a;
  --bg:#e9e6e1;
}
*{box-sizing:border-box;margin:0;padding:0}
html,body{width:1200px;height:900px;overflow:hidden;background:var(--bg);font-family:"Montserrat",sans-serif;color:var(--ink)}
.canvas{position:relative;width:1200px;height:900px}
.spread{position:absolute;left:20px;width:1160px;height:425px;overflow:hidden;box-shadow:0 4px 14px rgba(0,0,0,.18)}
.spread--outside{top:15px}
.spread--inside{top:460px;background:var(--green)}
.panel{position:absolute;top:0;width:386.67px;height:425px;overflow:hidden}
.panel--flap{left:0;background:var(--white)}
.panel--back{left:386.67px;background:var(--green)}
.panel--cover{left:773.34px;background:var(--white)}
.fold{position:absolute;top:0;width:1px;height:100%;background:rgba(0,0,0,.12)}
.abs{position:absolute}
.wave{position:absolute;left:0;width:100%}

/* flap */
.flap-intro{left:28px;top:20px;width:330px;font-size:10px;font-weight:700;line-height:1.35;text-align:center}
.flap-intro p+p{margin-top:8px;font-weight:600}
.checklist{left:28px;top:92px;width:335px;list-style:none}
.checklist li{position:relative;padding-left:18px;font-size:8.5px;line-height:1.35;margin-bottom:8px}
.checklist li svg{position:absolute;left:0;top:1px}
.checklist b{color:var(--purple-mid)}
.flap-foot{left:0;top:310px;width:100%;height:115px;background:var(--green)}
.flap-question{left:0;top:328px;width:100%;text-align:center;color:var(--white);font-weight:700;font-size:16px;line-height:1.15}
.flap-band{left:0;top:372px;width:100%;height:22px;background:var(--purple);color:var(--white);font-weight:700;font-size:13px;text-align:center;line-height:22px}
.flap-personal{left:0;top:398px;width:100%;text-align:center;color:var(--white);font-style:italic;font-weight:700;font-size:14px}

/* back */
.back-lead{left:20px;top:12px;width:340px;color:var(--white);font-style:italic;font-weight:500;font-size:11.5px;line-height:1.3}
.portrait{left:34px;top:72px;width:150px;height:150px;border-radius:50%;border:6px solid var(--purple);background:radial-gradient(circle at 50% 40%,#d8c2b0,#8c9ba3)}
.back-promise{left:190px;top:180px;width:175px;color:var(--white);font-style:italic;font-size:9px;line-height:1.3;text-align:right}
.seal{left:22px;top:222px;width:78px;height:78px;border-radius:50%;background:var(--gold);border:4px solid #b12a2a}
.back-contact{left:0;top:262px;width:100%;height:126px;background:var(--white)}
.back-call{left:0;top:280px;width:100%;text-align:center;font-size:9.5px;font-weight:600;line-height:1.25}
.back-phone{left:0;top:318px;width:100%;text-align:center;font-size:26px;font-weight:800;color:var(--purple)}
.back-address{left:0;top:352px;width:100%;text-align:center;font-size:9px;font-weight:600;line-height:1.25}
.back-foot{left:0;top:388px;width:100%;height:37px;background:var(--purple);color:var(--white);text-align:center}
.back-foot strong{display:block;font-size:13px;font-weight:700;padding-top:5px}
.back-foot span{font-size:9px}

/* cover */
.brand{left:0;top:20px;width:100%;text-align:center;font-size:22px;font-weight:500;color:var(--purple)}
.brand-dot{display:inline-block;width:12px;height:12px;border-radius:50%;background:var(--purple);margin-right:8px;vertical-align:middle}
.cover-band{left:0;top:68px;width:100%;height:96px;background:var(--purple)}
.cover-head{left:22px;top:92px;width:340px;color:var(--white);border-left:2px solid var(--white);padding-left:8px}
.cover-head strong{display:block;font-size:20px;font-weight:700;line-height:1.1}
.cover-head em{display:block;font-style:normal;font-size:17px;font-weight:700}
.cover-head span{display:block;font-size:13.5px;font-weight:400}
.baby-photo{left:0;top:164px;width:100%;height:110px;background:linear-gradient(135deg,#c9a48f,#e7d2c2 55%,#a9a09c)}
.cover-green{left:0;top:262px;width:100%;height:163px;background:var(--green)}
.cover-diff{left:0;top:270px;width:100%;text-align:center;color:var(--white);font-style:italic}
.cover-diff small{display:block;font-size:11px;font-weight:500}
.cover-diff strong{display:block;font-size:15px;font-weight:800}
.cover-ribbon{left:30px;top:306px;width:326px;height:16px;background:var(--white);color:var(--green);font-style:italic;font-weight:800;font-size:10.5px;text-align:center;line-height:16px}
.cover-list{left:0;top:322px;width:100%;height:44px;background:var(--purple);color:var(--white);text-align:center;padding-top:4px}
.cover-list strong{display:block;font-size:9.5px;font-weight:700}
.cover-list span{display:block;font-size:7px;line-height:1.25}
.cover-contact{left:0;top:368px;width:100%;text-align:center;color:var(--white)}
.cover-contact small{display:block;font-size:7.5px;font-style:italic}
.cover-contact strong{display:block;font-size:22px;font-weight:800;line-height:1}
.cover-contact span{display:block;font-size:10.5px;font-weight:700;margin-top:2px}

/* inside */
.inside-head{left:40px;top:22px;width:1080px;text-align:center;color:var(--white);font-weight:700;font-size:17px;line-height:1.35}
.promise-box{top:78px;width:330px;height:92px;background:var(--purple);border-radius:10px;color:var(--white);font-size:9px;line-height:1.35;text-align:center;padding:16px 18px;display:flex;align-items:center}
.inside-resources{left:60px;top:178px;width:1040px;text-align:center;color:var(--cream);font-weight:700;font-size:17px;line-height:1.35}
.delivery-seal{left:275px;top:228px;width:95px;height:95px;border-radius:50%;background:radial-gradient(circle,#cfcfcf,#8d8d8d);border:5px solid #b12a2a}
.talk{left:720px;top:236px;width:300px;text-align:center;color:var(--white)}
.talk strong{display:block;font-style:italic;font-weight:800;font-size:14px}
.talk span{display:block;font-size:9.5px;font-weight:600;line-height:1.3}
.stars{left:790px;top:276px;letter-spacing:2px;color:var(--gold);font-size:16px}
.reviews{left:735px;top:294px;width:245px;border:1.5px solid var(--white);border-top:none;color:var(--white);font-size:9.5px;font-weight:600;text-align:center;padding:4px 6px;line-height:1.25}
.couple-photo{left:0;top:300px;width:800px;height:125px;background:linear-gradient(100deg,#b8aea6,#eae4de 45%,#c3b2a5)}
.inside-contact{left:790px;top:300px;width:370px;height:125px;background:var(--cream)}
.inside-contact-text{left:840px;top:337px;width:300px;text-align:right;color:var(--purple);font-weight:800}
.inside-contact-text small{display:block;font-size:11px}
.inside-contact-text strong{display:block;font-size:22px;line-height:1.05}
.inside-contact-text span{display:block;font-size:13px}
</style>
</head>
<body>
<main class="canvas">

  <section class="spread spread--outside" aria-label="Brochure outside">
    <div class="panel panel--flap">
      <div class="abs flap-intro">
        <p>Anyone can give you CPAP Supplies. However we are committed to providing you with exceptional customer service too.</p>
        <p>How do we do this? By giving you services no other CPAP retailer offers, like...</p>
      </div>
      <ul class="abs checklist">
        <li><svg width="11" height="11" viewBox="0 0 12 12"><circle cx="6" cy="6" r="5" fill="none" stroke="#2f8a3c" stroke-width="1.3"/><path d="M3.3 6.2l2 2 3.6-4" fill="none" stroke="#2f8a3c" stroke-width="1.5"/></svg><b>Free Home Visits:</b> We bring the store to you so we can give you as much time as you need and set up all your equipment and supplies for you.</li>
        <li><svg width="11" height="11" viewBox="0 0 12 12"><circle cx="6" cy="6" r="5" fill="none" stroke="#2f8a3c" stroke-width="1.3"/><path d="M3.3 6.2l2 2 3.6-4" fill="none" stroke="#2f8a3c" stroke-width="1.5"/></svg><b>Free Delivery:</b> So you never need to come to the store (Unless you want to!).</li>
        <li><svg width="11" height="11" viewBox="0 0 12 12"><circle cx="6" cy="6" r="5" fill="none" stroke="#2f8a3c" stroke-width="1.3"/><path d="M3.3 6.2l2 2 3.6-4" fill="none" stroke="#2f8a3c" stroke-width="1.5"/></svg><b>Night and Weekend Appointments:</b> Because not everyone works 9-to-5.</li>
        <li><svg width="11" height="11" viewBox="0 0 12 12"><circle cx="6" cy="6" r="5" fill="none" stroke="#2f8a3c" stroke-width="1.3"/><path d="M3.3 6.2l2 2 3.6-4" fill="none" stroke="#2f8a3c" stroke-width="1.5"/></svg><b>A Dedicated Clinician:</b> Because we also want to be your friend.</li>
        <li><svg width="11" height="11" viewBox="0 0 12 12"><circle cx="6" cy="6" r="5" fill="none" stroke="#2f8a3c" stroke-width="1.3"/><path d="M3.3 6.2l2 2 3.6-4" fill="none" stroke="#2f8a3c" stroke-width="1.5"/></svg><b>Hardship and Financial-assistance Programs:</b> To make sure everyone gets the care they need.</li>
        <li><svg width="11" height="11" viewBox="0 0 12 12"><circle cx="6" cy="6" r="5" fill="none" stroke="#2f8a3c" stroke-width="1.3"/><path d="M3.3 6.2l2 2 3.6-4" fill="none" stroke="#2f8a3c" stroke-width="1.5"/></svg><b>Promise of Guaranteed Success:</b> We offer 30-day guarantees on all supplies so you know you are getting the best care possible.</li>
      </ul>
      <div class="abs flap-foot"></div>
      <svg class="wave" style="top:292px" width="387" height="30" viewBox="0 0 387 30" preserveAspectRatio="none"><path d="M0 18 Q100 0 200 14 T387 10 V30 H0Z" fill="#2f8a3c"/></svg>
      <div class="abs flap-question">Why are YOU<br>Settling for LESS?</div>
      <div class="abs flap-band">Let US treat you RIGHT!</div>
      <div class="abs flap-personal">We Make CPAP Personal!</div>
    </div>

    <div class="panel panel--back">
      <p class="abs back-lead">CPAP Doesn't need to be like this!<br>Let us make sure this doesn't<br>happen to you</p>
      <div class="abs portrait" role="img" aria-label="Photo of a man wearing a full CPAP mask, looking alarmed"></div>
      <p class="abs back-promise">We Guarantee Your CPAP Success, because your Success is our Reputation.</p>
      <svg class="wave" style="top:240px" width="387" height="26" viewBox="0 0 387 26" preserveAspectRatio="none"><path d="M0 22 Q120 4 240 14 T387 6 V26 H0Z" fill="#ffffff"/><path d="M0 22 Q120 4 240 14 T387 6" fill="none" stroke="#4a2a5c" stroke-width="5"/></svg>
      <div class="abs back-contact"></div>
      <div class="abs seal" role="img" aria-label="Satisfaction guarantee seal"></div>
      <p class="abs back-call">Call for an Appointment<br>(Or just to talk)<br>Today RestWell Supply</p>
      <p class="abs back-phone">905-555-0148</p>
      <p class="abs back-address">48 Harbour Lane<br>Port Elgin, Ontario N0H 2C0<br>Serving all of Ontario</p>
      <div class="abs back-foot"><strong>www.restwellsupply.com</strong><span>We Bring The Store To You</span></div>
    </div>

    <div class="panel panel--cover">
      <p class="abs brand"><span class="brand-dot"></span>RestWell Supply</p>
      <div class="abs cover-band"></div>
      <svg class="wave" style="top:56px" width="387" height="20" viewBox="0 0 387 20" preserveAspectRatio="none"><path d="M0 14 Q110 0 220 10 T387 6 V20 H0Z" fill="#4a2a5c"/></svg>
      <div class="abs cover-head"><strong>Want To Sleep</strong><em>Like A Baby Again?</em><span>Let us show You How!</span></div>
      <div class="abs baby-photo" role="img" aria-label="Photo of a newborn baby sleeping peacefully on a soft blanket"></div>
      <div class="abs cover-green"></div>
      <svg class="wave" style="top:246px" width="387" height="24" viewBox="0 0 387 24" preserveAspectRatio="none"><path d="M0 20 Q140 0 260 12 T387 4 V24 H0Z" fill="#2f8a3c"/><path d="M0 20 Q140 0 260 12 T387 4" fill="none" stroke="#4a2a5c" stroke-width="6"/></svg>
      <div class="abs cover-diff"><small>What Makes us Different?</small><strong>EVERYTHING!</strong></div>
      <div class="abs cover-ribbon">Free Home Visits &amp; Delivery</div>
      <div class="abs cover-list"><strong>Night and weekend appointments</strong><span>We specialize exclusively in Sleep Therapy</span><span>A dedicated clinician assigned directly to you</span><span>Hardship and financial-assistance programs</span></div>
      <div class="abs cover-contact"><small>We Bring The Store To You</small><strong>905-555-0148</strong><small>Serving all of Ontario</small><span>www.restwellsupply.com</span></div>
    </div>

    <div class="fold" style="left:386.67px"></div>
    <div class="fold" style="left:773.34px"></div>
  </section>

  <section class="spread spread--inside" aria-label="Brochure inside">
    <h2 class="abs inside-head">When you get diagnosed with Obstructive Sleep Apnea it can<br>be overwhelming. We are here to help. We will:</h2>
    <div class="abs promise-box" style="left:22px">Visit you in the comfort of your own home so we can privately discuss Sleep Apnea, explain what to expect next, and answer any and all your questions in a relaxed, comfortable environment. You don't get this from any other CPAP Retailer.</div>
    <div class="abs promise-box" style="left:415px">Figure out the best equipment and supplies you need to guarantee your success. We will even set up everything for you before we leave so you know it is set up right!</div>
    <div class="abs promise-box" style="left:808px">We are committed to your success. We will spend as much time with you as necessary to make sure all your questions are answered and every concern is addressed.</div>
    <p class="abs inside-resources">There are many resources available for you on<br>our website at www.restwellsupply.com.</p>
    <div class="abs delivery-seal" role="img" aria-label="Free delivery seal"></div>
    <div class="abs talk"><strong>WE LOVE TO TALK.</strong><span>You don't have to be a customer to call us, we will answer any questions you have!</span></div>
    <div class="abs stars" aria-label="Five stars">★★★★★</div>
    <p class="abs reviews">Check out our 5-Star reviews on ReviewHub<br>(By Searching for RestWell Supply)!</p>
    <div class="abs couple-photo" role="img" aria-label="Photo of a couple resting in bed, the man sleeping with a nasal CPAP mask"></div>
    <div class="abs inside-contact"></div>
    <svg class="wave" style="top:278px" width="1160" height="40" viewBox="0 0 1160 40" preserveAspectRatio="none"><path d="M0 30 Q250 0 520 22 T1160 12 V0 H0Z" fill="#2f8a3c"/><path d="M0 30 Q250 0 520 22 T1160 12" fill="none" stroke="#4a2a5c" stroke-width="9"/></svg>
    <div class="abs inside-contact-text"><small>www.restwellsupply.com</small><strong>905-555-0148</strong><span>Serving All Of Ontario</span></div>
    <div class="fold" style="left:386.67px"></div>
    <div class="fold" style="left:773.34px"></div>
  </section>

</main>
</body>
</html>
```